Web Design Project for starting CCTV/Camera security installer/reseller

Hello,

An old class mate is starting his own little CCTV/Camera security business as a one-man-gang.

He asked me to do his website but unfortunatly my design skills are not worth looking at :) The coding is no problem.

So I'm here to request a design.

What he wants is a site that lists the products he might install which is based on a small tree structure. So see it as a shop overview/display but without the baskets & cashout options.

you can find a site structure scheme, logo, product images & data sheet pdf's at this filebarn address:

https://www.filebarn.example/sh/kx7pq2931rv4zt8/wnLpHsRa3u/Vizor-Guard

the site itself is http://www.vizor-guard.example but only has a splash screen until I have a design for it.

the logo is a bit out of proportions, not sure if you can make something good out of it :/

Most content is in Dutch, I'll see if I can translate the needed parts...
Updates

Dear designers,

I have some good new for you.

You are allowed to use only that chrome Vizor-Guard part of the logo,
which should make things a lot easier to fit into your design ideas.

Keep up the creativity!

Dear designers,

I uploaded a new logo to the filebarn space.

It's a png but unfortunately it's not transparent, I'm still waiting for that one
but you know how to erase it in photoshop.

Target Market(s)

people looking for a visual solution to protect their company/home

Industry/Entity Type

Security

Requirements
Must have
• an iconized way to browse/display a tree. (not the traditional folder/explorer style)

maybe first a page with buttons/icons showing level 1 the group types (IP cams, IP servers, Accessories)

level 2 product groups (dome cam, ptz cam etc)

level 3 the actual product + a link to a pdf datasheet (if any)

could be multipage or maybe in/on-page since the product list won't be that huge.

maybe some random product info left and/or right so that the content area is not massive since he has not much to type
;)

```html
<!DOCTYPE html>
<html lang="en">
<head>
<meta charset="utf-8">
<title>Vizor-Guard — Camera Surveillance</title>
<link rel="stylesheet" href="https://fonts.googleapis.com/css2?family=Anton&family=Roboto:wght@300;400;700&family=Signika:wght@300;400;600&family=Lora:ital,wght@1,400;1,700&display=swap">
<style>
  :root {
    --black: #000;
    --ink: #222;
    --grey-text: #6b6b6b;
    --page: #efefef;
    --sky-top: #ffffff;
    --sky-bottom: #a9cff5;
    --brand-blue: #0aacf5;
    --brand-blue-light: #5ecdfd;
    --stat-blue: #3db4ef;
    --stat-label: #c9c9c9;
    --orange: #ff6a00;
    --orange-dark: #e23e00;
    --red-border: #d8230b;
    --gold: #ffd21f;
    --quote-name: #8a6a12;
    --footer-top: #3d3d3d;
    --footer-bottom: #000;
    --link-orange: #f4a21e;
    --chevron: #f2c53a;
  }
  * { box-sizing: border-box; margin: 0; padding: 0; }
  html, body { width: 1054px; height: 1200px; overflow: hidden; }
  body {
    position: relative;
    font-family: "Roboto", sans-serif;
    background: var(--page);
    color: var(--ink);
  }
  .sky {
    position: absolute; left: 0; top: 36px; width: 1054px; height: 300px;
    background: linear-gradient(var(--sky-top) 0%, var(--sky-top) 35%, var(--sky-bottom) 100%);
  }
  .topbar {
    position: absolute; left: 0; top: 0; width: 1054px; height: 36px;
    background: var(--black); color: #aaa; font-size: 10px;
  }
  .topbar .welcome { position: absolute; left: 115px; top: 12px; letter-spacing: .5px; }
  .topbar .welcome b { color: #fff; font-weight: 700; margin: 0 3px; }
  .topbar .account { position: absolute; right: 115px; top: 11px; font-size: 10px; font-weight: 700; color: #fff; }
  .topbar .account .login { color: var(--link-orange); }

  .logo {
    position: absolute; left: 118px; top: 72px; display: flex; align-items: center; gap: 8px;
    font-family: "Signika", sans-serif; font-size: 17px; font-weight: 400; color: #1c3f78;
  }
  .logo .mark { width: 14px; height: 14px; border-radius: 50%; background: #1c3f78; }

  .mainnav {
    position: absolute; left: 459px; top: 100px; width: 480px; height: 45px;
    background: var(--brand-blue); border-radius: 8px 8px 0 0;
    display: flex; align-items: center; justify-content: space-around; padding: 0 4px;
    font-family: "Roboto", sans-serif; font-size: 14px;
  }
  .mainnav a { color: #000; text-decoration: none; padding: 3px 7px; }
  .mainnav a.active { background: #000; color: #fff; border-radius: 2px; }

  .hero {
    position: absolute; left: 115px; top: 144px; width: 824px; height: 333px;
    background: radial-gradient(circle at 78% 40%, var(--brand-blue-light) 0%, var(--brand-blue) 55%);
    border-radius: 0 0 12px 12px; overflow: hidden;
    box-shadow: 0 8px 10px -6px rgba(0,0,0,.55);
  }
  .hero .corner-tl { position: absolute; left: 0; top: 0; }
  .hero .corner-br { position: absolute; right: 0; bottom: 0; }
  .hero .lead { position: absolute; left: 39px; top: 86px; font-family: "Signika", sans-serif; font-weight: 300; font-size: 22px; color: #fff; }
  .hero h1 { position: absolute; left: 38px; top: 103px; font-family: "Anton", sans-serif; font-weight: 400; font-size: 59px; line-height: 1.1; color: #000; letter-spacing: -.5px; white-space: nowrap; }
  .hero .sub { position: absolute; left: 39px; top: 166px; font-family: "Signika", sans-serif; font-size: 21px; color: #000; }
  .hero .note { position: absolute; left: 40px; top: 204px; font-family: "Signika", sans-serif; font-weight: 300; font-size: 16.5px; color: #fff; }
  .btn-read {
    position: absolute; left: 40px; top: 251px; width: 108px; height: 35px;
    background: linear-gradient(var(--orange), var(--orange-dark)); border: 1px solid var(--red-border);
    border-radius: 4px; color: #fff; font-weight: 700; font-size: 16px; text-align: center; line-height: 33px;
  }
  .hero .product-photo {
    position: absolute; left: 461px; top: 86px; width: 313px; height: 206px;
    background: linear-gradient(160deg, rgba(255,255,255,.55), rgba(210,218,226,.45));
  }
  .slider-dots { position: absolute; left: 496px; top: 494px; display: flex; gap: 4px; }
  .slider-dots span { width: 9px; height: 9px; border-radius: 50%; background: #000; }
  .slider-dots span.on { background: #c64512; }

  .intro h2 { position: absolute; left: 122px; top: 548px; font-family: "Signika", sans-serif; font-weight: 300; font-size: 33px; color: #333; }
  .intro h2 b { font-weight: 400; color: #000; }
  .intro p { position: absolute; left: 119px; width: 430px; font-size: 11.5px; font-weight: 300; line-height: 1.25; color: var(--grey-text); }
  .intro .p1 { top: 611px; }
  .intro .p2 { top: 653px; }
  .sample-label { position: absolute; left: 571px; top: 640px; width: 80px; height: 70px; background: rgba(232,64,28,.12); border-radius: 6px; }
  .sample-arrow { position: absolute; left: 610px; top: 610px; }
  .video {
    position: absolute; left: 657px; top: 560px; width: 282px; height: 197px;
    background: #fff; padding: 5px; box-shadow: 0 0 3px rgba(0,0,0,.15);
  }
  .video .screen { width: 100%; height: 100%; background: #000; display: flex; align-items: center; justify-content: center; }

  .stats {
    position: absolute; left: 115px; top: 790px; width: 824px; height: 105px; background: #000;
  }
  .stat { position: absolute; top: 28px; font-family: "Signika", sans-serif; }
  .stat .num { display: block; font-size: 25px; font-weight: 600; color: var(--stat-blue); line-height: 1; }
  .stat .label { display: block; font-size: 15px; font-weight: 300; color: var(--stat-label); margin-top: 6px; letter-spacing: .3px; }
  .stats .chevron { position: absolute; left: 506px; top: 28px; }
  .btn-signup {
    position: absolute; left: 608px; top: 19px; width: 194px; height: 66px;
    background: linear-gradient(#ff7a12, var(--orange-dark)); border: 2px solid var(--red-border); border-radius: 5px;
    font-family: "Signika", sans-serif; color: #fff;
  }
  .btn-signup .play { position: absolute; left: 12px; top: 15px; }
  .btn-signup .big { position: absolute; left: 36px; top: 10px; font-size: 25px; }
  .btn-signup .small { position: absolute; left: 39px; top: 44px; font-size: 9.5px; color: #2a0a00; font-weight: 600; letter-spacing: .3px; }

  .section-title { position: absolute; top: 935px; font-family: "Signika", sans-serif; font-weight: 600; font-size: 31px; color: #4a4a4a; }
  .featured-title { left: 115px; }
  .feedback-title { left: 645px; }
  .carousel-arrow { position: absolute; top: 1017px; }
  .thumb {
    position: absolute; top: 989px; width: 108px; height: 79px; border: 1px solid #ddd;
    background: linear-gradient(135deg, #fafafa, #d8d8d8);
  }
  .quote-mark { position: absolute; left: 651px; top: 998px; font-family: "Lora", serif; font-size: 90px; color: #cfcfcf; line-height: 1; }
  .quote-rule { position: absolute; left: 711px; top: 984px; width: 2px; height: 93px; background: #999; }
  .quote-text { position: absolute; left: 729px; top: 982px; width: 210px; font-family: "Roboto", sans-serif; font-style: italic; font-weight: 300; font-size: 11px; line-height: 1.3; color: #333; letter-spacing: .3px; }
  .quote-name { position: absolute; left: 726px; top: 1041px; font-family: "Lora", serif; font-style: italic; font-size: 18px; color: var(--quote-name); }
  .quote-place { position: absolute; left: 726px; top: 1065px; font-family: "Lora", serif; font-style: italic; font-size: 11px; color: #222; }

  .footer-links {
    position: absolute; left: 0; top: 1112px; width: 1054px; height: 49px; background: var(--footer-top);
    display: flex; justify-content: center; align-items: center; gap: 10px;
    font-size: 11.5px; font-weight: 700; color: #fff;
  }
  .footer-links .sep { color: #bbb; font-weight: 400; }
  .footer-bottom { position: absolute; left: 0; top: 1161px; width: 1054px; height: 39px; background: var(--footer-bottom); font-size: 10px; }
  .copyright { position: absolute; left: 129px; top: 15px; color: #777; }
  .copyright u { color: #ccc; }
  .newsletter { position: absolute; left: 331px; top: 7px; display: flex; align-items: center; gap: 5px; color: var(--link-orange); font-size: 10.5px; }
  .newsletter .field { width: 179px; height: 24px; background: #f4f4f4; border: 1px solid #ccc; }
  .newsletter .submit { width: 55px; height: 24px; background: var(--gold); color: #000; font-weight: 700; font-size: 11px; text-align: center; line-height: 24px; border-radius: 2px; margin-left: 2px; }
  .social { position: absolute; left: 853px; top: 7px; display: flex; gap: 6px; }
  .social span { width: 22px; height: 22px; border-radius: 50%; background: #777; }
</style>
</head>
<body>
  <div class="sky"></div>

  <header class="topbar">
    <div class="welcome">Welcome at <b>Vizor-Guard</b> Camera Surveilance.</div>
    <div class="account"><span class="login">Login</span> &nbsp;|&nbsp; Sign Up</div>
  </header>

  <div class="logo"><span class="mark"></span>Vizor-Guard</div>

  <nav class="mainnav">
    <a class="active">Home</a><a>Products</a><a>Tips</a><a>Installation</a><a>Contact</a>
  </nav>

  <section class="hero">
    <svg class="corner-tl" width="56" height="56"><polygon points="0,0 56,0 0,56" fill="#000"/></svg>
    <svg class="corner-br" width="56" height="56"><polygon points="56,0 56,56 0,56" fill="#000"/></svg>
    <p class="lead">Are you looking for a</p>
    <h1>CAMERA SYSTEM</h1>
    <p class="sub">for your home or company?</p>
    <p class="note">Then you are at Vizor-Guard at the right address!</p>
    <div class="btn-read">Read More</div>
    <div class="product-photo" role="img" aria-label="Product photo of a white box-style security camera"></div>
  </section>

  <div class="slider-dots"><span class="on"></span><span></span><span></span><span></span><span></span></div>

  <section class="intro">
    <h2>Welcome to <b>Vizor-Guard</b></h2>
    <p class="p1">We offer a large amount of surveilance camera's, video storage systems and surveilance monitors.</p>
    <p class="p2">But we also have complete camera surveillance sets for you (analogue or IP camera's) including the cables and power supplies, so that you don't have to worry about additional components when ordering.</p>
  </section>

  <div class="sample-label" role="img" aria-label="Hand-lettered note: View Sample Footage"></div>
  <svg class="sample-arrow" width="50" height="40" viewBox="0 0 50 40">
    <path d="M4 36 Q24 24 44 6" stroke="#e8401c" stroke-width="2" fill="none"/>
    <path d="M36 5 L45 5 L43 14" stroke="#e8401c" stroke-width="2" fill="none"/>
  </svg>

  <div class="video">
    <div class="screen">
      <svg width="52" height="58" viewBox="0 0 52 58"><path d="M4 3 Q4 0 7 2 L50 27 Q52 29 50 31 L7 56 Q4 58 4 55 Z" fill="#fff"/></svg>
    </div>
  </div>

  <section class="stats">
    <div class="stat" style="left:25px"><span class="num">591</span><span class="label">Customers</span></div>
    <div class="stat" style="left:162px"><span class="num">268</span><span class="label">Camera Items</span></div>
    <div class="stat" style="left:331px"><span class="num">3589</span><span class="label">Camera Installations</span></div>
    <svg class="chevron" width="30" height="52"><polyline points="3,2 27,26 3,50" stroke="var(--chevron)" stroke-width="2.5" fill="none"/></svg>
    <div class="btn-signup">
      <svg class="play" width="20" height="20"><circle cx="10" cy="10" r="10" fill="#111"/><polygon points="8,6 14,10 8,14" fill="#fff"/></svg>
      <span class="big">Sign Up Now</span>
      <span class="small">Set Your Own Camera System</span>
    </div>
  </section>

  <h3 class="section-title featured-title">Featured Products</h3>
  <svg class="carousel-arrow" style="left:111px" width="14" height="22"><polyline points="12,2 3,11 12,20" stroke="var(--brand-blue)" stroke-width="2.5" fill="none"/></svg>
  <div class="thumb" style="left:132px" role="img" aria-label="Photo of a compact cube camera"></div>
  <div class="thumb" style="left:248px" role="img" aria-label="Photo of a dome camera"></div>
  <div class="thumb" style="left:365px" role="img" aria-label="Photo of a PTZ camera"></div>
  <div class="thumb" style="left:482px" role="img" aria-label="Photo of a bullet camera"></div>
  <svg class="carousel-arrow" style="left:598px" width="14" height="22"><polyline points="2,2 11,11 2,20" stroke="var(--brand-blue)" stroke-width="2.5" fill="none"/></svg>

  <h3 class="section-title feedback-title">Client Feedback</h3>
  <div class="quote-mark">&ldquo;</div>
  <div class="quote-rule"></div>
  <p class="quote-text">Lorem ipsum dolor sit amet, consectetur adipiscing elit. Fusce iaculis fringilla vehicula. Cras vel turpis vel justo luctus viverra id non magna.</p>
  <p class="quote-name">Daan Verhoeven</p>
  <p class="quote-place">Glasgow, UK.</p>

  <footer>
    <nav class="footer-links">
      <span>Home</span><span class="sep">::</span><span>About Us</span><span class="sep">::</span><span>Products</span><span class="sep">::</span><span>Tips</span><span class="sep">::</span><span>Installation</span><span class="sep">::</span><span>Contact</span><span class="sep">::</span><span>Privacy Policy</span><span class="sep">:::</span><span>Terms of use</span>
    </nav>
    <div class="footer-bottom">
      <div class="copyright">Copyright 2012 @ <u>Vizor-Guard</u></div>
      <div class="newsletter">Sign Up for Newsletter: <span class="field"></span><span class="submit">Submit</span></div>
      <div class="social"><span></span><span></span><span></span></div>
    </div>
  </footer>
</body>
</html>
```